Flyer for Holiday Promotion: Dog Related

We are in need of a flyer for our Dog Daycare, Boarding, and Grooming facility. We are a 'pet resort focused on the wellness and happiness of each of our canine guests. The Holidays are coming up and we would like a design to promote our boarding services between Thanksgiving and New Years Eve.

We would like to see designs that are professional and comforting to pet parents to create a high level of trust. The design should include the required information and a photo of pets around the Holiday time frame. All photos used should not be clip art or cartoon-ish, Please use real images that create excitement and do not look to 'stock photo'.

Target Market(s)

We will be handing the flyers our to Veterinarians and to area school districts.

Industry/Entity Type

Pet

Requirements
Must have
• Our Holiday Offer: Special Holiday Rate of $29.00 per pet night
Includes: Unlimited supervised play, plush dog beds, nightly tuck in, and more
Offer Date: November 1 January 2nd

Extra events we are offering so have an area that says something like: Be sure to sign up for: Thanksgiving Dinner Buffet, Milk and Cookies with Santa, Christmas Brunch, Stocking Suffers and More.

Offer restrictions: Based on availability, not valid with any other offers or promotions, some exclusions may apply, please contact us for details. Must mention offer at time of booking.

Please include our logo: I will attach it.
Our Name: The Maple Kennel
Address: 2847 Orchard Lane Neenah, WI 54873
Phone: 920-555-0148
Web: www.MapleKennelStays.example
All of our services: Dog Daycare, Overnight Care, Grooming

Can come up with a catchy slogan or saying, such as: Holidays at The Maple Kennel, Holiday Hounds. Or a bit more creative than I can come up with!!
Should not have
• Clip art

```html
<!DOCTYPE html>
<html lang="en">
<head>
<meta charset="utf-8">
<title>Holidays At: The Maple Kennel</title>
<link rel="stylesheet" href="https://fonts.googleapis.com/css2?family=Arimo:wght@400&family=EB+Garamond:ital@1&family=Parisienne&family=Raleway:wght@200;400&display=swap">
<style>
  :root {
    --page-grey: #a3a3a3;
    --hero-dark: #3e3e3e;
    --hero-mid: #6a6a6a;
    --hero-light: #8d8d8d;
    --offer-tan: #e4c698;
    --events-green: #98cf98;
    --ink: #111111;
    --white: #ffffff;
    --brand-teal: #a9dde3;
    --mark-dark: #1f2a22;
  }
  * { box-sizing: border-box; margin: 0; padding: 0; }
  html, body { width: 927px; height: 1200px; overflow: hidden; }
  body {
    position: relative;
    background: var(--page-grey);
    font-family: "Arimo", Arial, sans-serif;
    color: var(--ink);
  }
  .hero-photo {
    position: absolute; left: 0; top: 0; width: 927px; height: 458px;
    background:
      radial-gradient(ellipse 320px 260px at 560px 170px, var(--hero-light), transparent 70%),
      radial-gradient(ellipse 260px 200px at 820px 120px, var(--hero-dark), transparent 75%),
      linear-gradient(160deg, var(--hero-dark) 0%, var(--hero-mid) 45%, var(--hero-dark) 100%);
  }
  .brand {
    position: absolute; left: 28px; top: 48px;
    display: flex; align-items: center; gap: 12px;
  }
  .brand-square { width: 56px; height: 56px; background: var(--brand-teal); }
  .brand-name {
    font-family: "Arimo", Arial, sans-serif; font-size: 22px;
    color: var(--brand-teal); letter-spacing: 1px;
  }
  .headline-script {
    position: absolute; left: 268px; top: 190px;
    font-family: "Parisienne", cursive; font-size: 112px; line-height: 1;
    color: var(--white); white-space: nowrap;
  }
  .headline-name {
    position: absolute; right: 60px; top: 300px;
    font-family: "Raleway", sans-serif; font-weight: 200; font-size: 86px;
    line-height: 1; color: var(--white); letter-spacing: 1px; white-space: nowrap;
  }
  .offer-panel {
    position: absolute; left: 60px; top: 472px; width: 867px; height: 337px;
    background: var(--offer-tan); border-radius: 3px 0 0 3px;
  }
  .offer-title {
    position: absolute; left: 62px; top: 22px;
    font-family: "Parisienne", cursive; font-size: 80px; line-height: 1;
    color: var(--white); white-space: nowrap;
  }
  .offer-dates {
    position: absolute; right: 59px; top: 133px;
    font-size: 25px; white-space: nowrap;
  }
  .offer-price {
    position: absolute; right: 59px; top: 166px;
    font-size: 31px; white-space: nowrap;
  }
  .offer-price .amount { font-family: "EB Garamond", serif; font-style: italic; font-size: 36px; }
  .offer-includes {
    position: absolute; left: 76px; top: 236px;
    font-size: 19.5px; white-space: nowrap;
  }
  .offer-terms {
    position: absolute; left: 134px; right: 49px; top: 299px;
    font-size: 13.2px; line-height: 1.2;
  }
  .events-panel {
    position: absolute; left: 60px; top: 832px; width: 867px; height: 203px;
    background: var(--events-green); border-radius: 3px 0 0 3px;
  }
  .events-mark {
    position: absolute; left: 64px; top: 24px; width: 134px; height: 124px;
    background: var(--mark-dark); opacity: 0.12; border-radius: 8px;
  }
  .events-title {
    position: absolute; right: 55px; top: 10px;
    font-family: "Parisienne", cursive; font-size: 50px; line-height: 1;
    white-space: nowrap;
  }
  .events-note {
    position: absolute; right: 77px; top: 72px;
    font-size: 17px; white-space: nowrap;
  }
  .events-list {
    position: absolute; right: 53px; top: 114px;
    font-size: 18px; line-height: 1.35; text-align: right; white-space: nowrap;
  }
  .footer {
    position: absolute; right: 55px; top: 1063px; text-align: right;
  }
  .footer-name { font-size: 29px; line-height: 1.15; }
  .footer-line { font-size: 14px; line-height: 1.45; }
</style>
</head>
<body>
  <div class="hero-photo" role="img" aria-label="Soft black-and-white holiday photo of a pet resting"></div>

  <div class="brand">
    <span class="brand-square"></span>
    <span class="brand-name">THE MAPLE KENNEL</span>
  </div>

  <h1>
    <span class="headline-script">Holidays At:</span>
    <span class="headline-name">THE MAPLE KENNEL</span>
  </h1>

  <section class="offer-panel">
    <h2 class="offer-title">Special Holiday Rate:</h2>
    <p class="offer-dates">November 1—January 2nd</p>
    <p class="offer-price"><span class="amount">$29.00</span> per pet night</p>
    <p class="offer-includes">Includes: Unlimited supervised play, plush dog beds, nightly tuck in, &amp; more.</p>
    <p class="offer-terms">Offer restrictions: Based on availability, not valid with any other offers or promotions, some exclusions may apply, please contact us for details. Must mention offer at time of booking.</p>
  </section>

  <section class="events-panel">
    <div class="events-mark" role="img" aria-label="Paw print decoration"></div>
    <h2 class="events-title">Upcoming Events:</h2>
    <p class="events-note">Be sure to sign up!</p>
    <p class="events-list">Thanksgiving Dinner Buffet, Milk &amp; Cookies with Santa,<br>Christmas Brunch, Stocking Stuffers &amp; MORE.</p>
  </section>

  <footer class="footer">
    <p class="footer-name">The Maple Kennel</p>
    <p class="footer-line">2847 Orchard Lane Neenah, WI 54873</p>
    <p class="footer-line">920-555-0148 | www.MapleKennelStays.example</p>
    <p class="footer-line">Daycare, Overnight Care &amp; Grooming</p>
  </footer>
</body>
</html>
```